Product label and brand logo for Superfood powder

We need a product label (incl. logo) for a new plant-based Superfood powder called "MyLumaRoot Health & Wellness Protein" ("MyLumaRoot" being the brand). The powder formula is comprised of various Superfoods that each offer a unique benefit to the customer. On top of that the formular includes real coffee for excellent taste. This is a premium product and some ingredients even come from organic sources. I've included an extended briefing with examples as a PDF. The final design should communicate wellbeing, health, wellness rather than target the sport and fitness crowd (as most protein powders do).
Target Market(s)
Health & Wellness Space
Industry/Entity Type
Health And Wellness
Requirements
Must have
- Please see attached PDF.
Nice to have

```html
<!DOCTYPE html>
<html lang="de">
<head>
<meta charset="utf-8">
<title>MyLumaRoot Health &amp; Wellness Protein – Etikett</title>
<link rel="stylesheet" href="https://fonts.googleapis.com/css2?family=Josefin+Sans:wght@300&family=Tenor+Sans&family=Source+Sans+3:wght@400;600&family=Merriweather:wght@700;900&display=swap">
<style>
  :root {
    --bg-page: #f2f0ee;
    --brown-deep: #2e150a;
    --brown-mid: #6b3512;
    --gold-text: #e8b865;
    --white: #ffffff;
    --table-line: #7a7a7a;
    --ink: #222222;
  }
  * { box-sizing: border-box; margin: 0; padding: 0; }
  html, body { width: 1200px; height: 1200px; overflow: hidden; background: var(--bg-page); }
  .canvas { position: relative; width: 1200px; height: 1200px; }
  .label {
    position: absolute; left: 20px; top: 278px; width: 1160px; height: 643px; overflow: hidden;
    color: var(--white);
    font-family: "Source Sans 3", sans-serif;
    background:
      radial-gradient(ellipse 320px 260px at 560px 40px, rgba(246,205,134,.85), rgba(246,205,134,0) 70%),
      radial-gradient(ellipse 700px 160px at 600px 360px, rgba(201,118,44,.55), rgba(201,118,44,0) 70%),
      linear-gradient(180deg, var(--brown-mid) 0%, #8a4a1c 45%, #4a2410 80%, var(--brown-deep) 100%);
  }
  .abs { position: absolute; }
  .centered { text-align: center; white-space: nowrap; }
  .brand-name { font-family: "Josefin Sans", sans-serif; font-weight: 300; letter-spacing: 1px; }
  .tagline { font-family: "Tenor Sans", sans-serif; }
  .product-title { font-family: "Tenor Sans", sans-serif; line-height: 1; }

  .front-brand { left: 141px; top: 88px; width: 300px; font-size: 46px; }
  .front-tagline { left: 121px; top: 212px; width: 340px; font-size: 32px; }
  .front-title { left: 91px; top: 250px; width: 400px; font-size: 80px; }
  .coffee-photo { left: 350px; top: 236px; }

  .stat { font-family: "Merriweather", serif; font-weight: 900; font-size: 42px; line-height: 1; }
  .stat-label { font-size: 15px; }
  .divider { width: 1px; height: 46px; background: var(--white); }
  .claims { left: 60px; top: 512px; font-size: 15px; }
  .pack-size { font-family: "Merriweather", serif; font-weight: 700; font-size: 13px; color: var(--gold-text); white-space: nowrap; }
  .vegan-seal { left: 384px; top: 417px; }

  .nutrition {
    left: 617px; top: 122px; width: 325px; border-collapse: collapse; background: var(--white);
    color: var(--ink); font-size: 7.5px; border: 1.5px solid var(--ink);
  }
  .nutrition th, .nutrition td { height: 16px; padding: 0 4px; text-align: left; border-bottom: 1px solid var(--table-line); }
  .nutrition th { font-weight: 600; }
  .nutrition .col-a { width: 160px; }
  .nutrition .col-b { width: 80px; }
  .body-copy { font-size: 15px; line-height: 19px; }

  .back-brand { left: 946px; top: 62px; width: 200px; font-size: 30px; }
  .back-tagline { left: 946px; top: 178px; width: 200px; font-size: 17px; }
  .back-title { left: 946px; top: 198px; width: 200px; font-size: 38px; }
  .flavour-ribbon { left: 920px; top: 494px; }
  .made-in { right: 64px; top: 588px; font-family: "Merriweather", serif; font-weight: 700; font-size: 14px; white-space: nowrap; }
  .flag { right: 16px; top: 587px; }
</style>
</head>
<body>
<main class="canvas">
  <section class="label" aria-label="Produktetikett MyLumaRoot Health &amp; Wellness Protein">
    <svg class="abs coffee-photo" width="210" height="200" viewBox="0 0 210 200" role="img" aria-label="Foto eines Haufens gerösteter Kaffeebohnen">
      <defs>
        <radialGradient id="beans" cx="50%" cy="50%" r="50%">
          <stop offset="0%" stop-color="#3b2214"/>
          <stop offset="70%" stop-color="#5a3722" stop-opacity=".9"/>
          <stop offset="100%" stop-color="#5a3722" stop-opacity="0"/>
        </radialGradient>
      </defs>
      <ellipse cx="105" cy="100" rx="104" ry="98" fill="url(#beans)"/>
    </svg>

    <div class="abs centered brand-name front-brand">MyLumaRoot</div>
    <div class="abs centered tagline front-tagline">Health &amp; Wellness</div>
    <div class="abs centered product-title front-title">PROTEIN</div>

    <div class="abs stat" style="left:60px;top:445px;">4g</div>
    <div class="abs stat-label" style="left:65px;top:489px;">BCAA</div>
    <div class="abs divider" style="left:128px;top:448px;"></div>
    <div class="abs stat" style="left:148px;top:445px;">4g</div>
    <div class="abs stat-label" style="left:145px;top:489px;">Glutamin</div>
    <div class="abs" style="left:214px;top:448px;font-size:30px;">+</div>
    <div class="abs stat-label" style="left:247px;top:459px;line-height:18px;">Vitamine<br>Mineralstoffe</div>
    <div class="abs claims">Laktosefrei | Glutenfree | Kein Zucker zugefügt</div>
    <div class="abs pack-size" style="left:172px;top:578px;">Glute 1.000g / 25 Portionenenfree</div>

    <svg class="abs vegan-seal" width="144" height="144" viewBox="0 0 144 144" aria-hidden="true">
      <circle cx="72" cy="72" r="70" fill="#3a1c0c"/>
      <circle cx="72" cy="72" r="50" fill="#f4ead6"/>
    </svg>

    <table class="abs nutrition">
      <tr><th class="col-a">Nährwete</th><th class="col-b">pro 100 g</th><th>pro 30 g</th></tr>
      <tr><td>Brennwert</td><td>1597 kJ</td><td>479 kJ</td></tr>
      <tr><td>Brennwert</td><td>378 kcal</td><td>113 kcal</td></tr>
      <tr><td>Fett</td><td>5.5 g</td><td>1.6 g</td></tr>
      <tr><td>- davon gesättigte Fettsauren</td><td>1.8 g</td><td>0.56 g</td></tr>
      <tr><td>Kohlenhydrate</td><td>3 g</td><td>0.92 g</td></tr>
      <tr><td>- davon Zucker</td><td>0 g</td><td>0 g</td></tr>
      <tr><td>Ballaststoffe</td><td>7.2 g</td><td>2.1 g</td></tr>
      <tr><td>Eiweiß</td><td>75.2 g</td><td>22.5 g</td></tr>
      <tr><td>Salz *</td><td>0.91 g</td><td>0.27 g</td></tr>
    </table>

    <div class="abs centered brand-name back-brand">MyLumaRoot</div>
    <div class="abs centered tagline back-tagline">Health &amp; Wellness</div>
    <div class="abs centered product-title back-title">PROTEIN</div>

    <p class="abs body-copy" style="left:617px;top:319px;width:250px;">Verzehrempfehlung: 40g Pulver im Shaker mit 400-500ml Wasser mischenund gut schütteln</p>
    <p class="abs body-copy" style="left:617px;top:400px;width:250px;">Mindestens haltbar bis Ende und Chargennummer: siehe Boden</p>
    <p class="abs body-copy" style="left:951px;top:319px;width:190px;">Zutaten:[Zutatenliste] Ingredients1, Ingredients2, Ingredients3, Ingredients4, Ingredients5.</p>
    <p class="abs body-copy" style="left:617px;top:494px;width:260px;">Vertrieb/Distributor: MyLumaRoot OG, Lindenweg 12, 4020 Linz, Österreich.<br>Telefon: +43 660 987654321<br>www.mylumaroot.example<br>www.social.example/mylumaroot</p>

    <svg class="abs flavour-ribbon" width="216" height="46" viewBox="0 0 216 46" role="img" aria-label="Zierband mit dem Hinweis Kaffeegeschmack">
      <path d="M10 14 Q108 2 206 14 L206 34 Q108 22 10 34 Z" fill="#a8702e"/>
    </svg>

    <div class="abs pack-size" style="right:16px;top:559px;font-family:'Source Sans 3',sans-serif;font-weight:400;font-size:15px;">Glute 1.000g / 25 Portionenenfree</div>
    <div class="abs made-in">Hergestellt in Deutschland</div>
    <svg class="abs flag" width="36" height="22" viewBox="0 0 36 22" aria-hidden="true">
      <rect width="36" height="7.4" fill="#000"/>
      <rect y="7.3" width="36" height="7.4" fill="#dd0000"/>
      <rect y="14.6" width="36" height="7.4" fill="#ffce00"/>
    </svg>
  </section>
</main>
</body>
</html>
```